Push notification screens at app start up

We have an existing news publication app platform and are adding categories to push notifications.

We need two screens designed (each for Novaro, Tavlet and Morvelin for a total of 6d) that show when the app is first launched.

The workflow of our app:
0. app launch screen while webservices run (no work needed)
1. information screen to the user promoting the benefits of push notification with "Next" button. (see concept attached)
2. Push categories selection screen. This will have list of category types, with on/off switch.

"Select the categories that you wish to receive occasional notices:
Breaking News (on/off switch)
Local News (on/off switch)
Sports (on/off switch)
Local Events (on/off switch)
Weather Alerts (on/off switch)
Local Deals (on/off switch)"

"Enable these categories on the next screen."
"Next" button

Background:
When I was looking around at app designs, I came across this one (http://www.pixelvane.net/design/7148305) and I really liked it. We obviously have different features on our screen, but I’d like to have this same feel. The colors used in this design are perfect.

UPDATE: I do not mean to limit your design to match the layout as the one mentioned above. Please use your creativity for the layout.

Our standard font in Helvetica Neue.

Notes:
- our app is developed for all phone devices from Novaro 4 to Novaro 6, so designs should be thoughtful of vertical scrolling if needed.
- our app is developed for Tavlets, so we'll need designs completed as well. (We can finalize Novaro design first, then translate the design to Tavlet.)
- our app is developed for Morvelin phones (not tablets), so we'll need designs completed as well. (We can finalize Kvo design first, then translater to Morvelin UI design guidelines).

We hope to establish a good on-going relationship with the designer for as-needed work in the future.

Industry/Entity Type

News

Font styles to use
Other font styles liked:
• Helvetica Neue

Requirements
Must have
• Clean designs. No clutter.
Nice to have
• We would likely go with the standard on/off switches for both Kvo and Morvelin, but are open to small custom variations.

```html
<!DOCTYPE html>
<html lang="en">
<head>
<meta charset="utf-8">
<title>Push Notification Screens</title>
<link rel="stylesheet" href="https://fonts.googleapis.com/css2?family=Roboto:wght@300;400;500&display=swap">
<style>
:root{
  --purple:#6a4fb4;
  --purple-deep:#4a2f8c;
  --purple-bar:#6447b0;
  --lilac:#d9cdee;
  --mist:#efeaf6;
  --teal-mist:#bfe3e6;
  --ink:#3a3a44;
  --ink-soft:#55555f;
  --white:#ffffff;
  --amber:#f2b51c;
  --amber-dark:#d99411;
  --alert:#e0282e;
  --off:#4b4b52;
  --line:#ececf2;
}
*{box-sizing:border-box;margin:0;padding:0}
html,body{width:699px;height:1200px;overflow:hidden;background:var(--white)}
body{position:relative;font-family:"Roboto",Helvetica,Arial,sans-serif;color:var(--ink)}
.screen{position:absolute;width:345px;height:594px;overflow:hidden;background:var(--white)}
.screen--tl{left:0;top:0}
.screen--tr{left:354px;top:0}
.screen--bl{left:0;top:606px}
.screen--br{left:354px;top:606px}
.backdrop{position:absolute;inset:0}
.backdrop--intro{background:linear-gradient(180deg,#6b55b6 0%,#8d7cc6 22%,#cfc3e6 45%,var(--mist) 62%,#f6f3fa 100%)}
.backdrop--intro-alt{background:linear-gradient(180deg,#6a52b4 0%,#9b86cc 30%,#d3c7ea 55%,#cfd9ee 75%,var(--teal-mist) 100%)}
.backdrop--header{height:150px;bottom:auto;background:linear-gradient(180deg,#5f46ad 0%,#8a74c8 100%)}
.backdrop--full{background:linear-gradient(180deg,#6046ae 0%,#7a63bf 40%,#8f7ccb 70%,#6a55b0 100%)}
.status-bar{position:absolute;top:0;left:0;right:0;height:20px;display:flex;align-items:center;justify-content:space-between;padding:0 6px;font-size:10px;color:var(--white);z-index:2}
.status-bar .time{position:absolute;left:0;right:0;text-align:center}
.battery{display:inline-block;width:18px;height:8px;border:1px solid var(--white);border-radius:2px;margin-left:3px;vertical-align:middle;background:var(--white);background-clip:content-box;padding:1px}
.intro-title{position:absolute;top:74px;left:0;right:0;text-align:center;font-weight:300;font-size:31px;letter-spacing:1px;color:var(--white)}
.bell-badge{position:absolute;left:108px;top:150px;width:130px;height:130px}
.intro-copy{position:absolute;left:58px;right:40px;font-size:12.5px;line-height:15.5px;text-align:justify;color:var(--ink-soft)}
.intro-copy p+p{margin-top:14px}
.intro-copy strong{font-weight:500;color:var(--purple-deep)}
.next-bar{position:absolute;left:0;right:0;bottom:0;height:48px;background:var(--purple-bar);color:var(--white);font-size:14px;font-weight:500;letter-spacing:.5px;display:flex;align-items:center;justify-content:center}
.next-bar--deep{background:var(--purple-deep)}
.next-button{position:absolute;left:20px;right:20px;top:515px;height:38px;border-radius:5px;background:var(--white);color:var(--purple);font-size:14px;font-weight:500;display:flex;align-items:center;justify-content:center;box-shadow:0 2px 6px rgba(60,40,120,.2)}
.app-header{position:absolute;top:26px;left:0;right:0;height:30px;display:flex;align-items:center;justify-content:center;color:var(--white);font-size:17px;z-index:2}
.app-header .back{position:absolute;left:10px;top:5px;width:20px;height:20px}
.prompt{position:absolute;left:20px;right:20px;text-align:center;color:var(--white)}
.prompt--small{top:62px;font-size:12px;line-height:15px}
.prompt--large{top:72px;font-size:15px;line-height:20px}
.mini-bell{position:absolute;left:137px;top:115px;width:72px;height:72px}
.category-list{position:absolute;left:0;right:0;top:196px;list-style:none}
.category-list li{height:40px;display:flex;align-items:center;padding:0 14px 0 16px;border-bottom:1px solid var(--line);font-size:14px;color:var(--ink)}
.category-list .icon{width:22px;height:22px;margin-right:16px;flex:none}
.category-list .label{flex:1}
.toggle{width:22px;height:22px;flex:none}
.enable-row{position:absolute;left:16px;right:10px;display:flex;align-items:center;font-size:11px}
.enable-row svg{width:18px;height:18px;margin-right:8px;flex:none}
.enable-row--list{top:466px;color:var(--ink)}
.enable-row--grid{top:470px;color:var(--white)}
.category-grid{position:absolute;left:14px;right:14px;top:158px;display:grid;grid-template-columns:repeat(3,1fr);row-gap:26px;list-style:none}
.category-grid li{display:flex;flex-direction:column;align-items:center;color:var(--white);font-size:11px;letter-spacing:.3px;text-transform:uppercase}
.category-grid .disc{width:64px;height:64px;border-radius:50%;background:var(--white);display:flex;align-items:center;justify-content:center;margin-bottom:8px;box-shadow:0 2px 6px rgba(30,10,80,.25)}
.category-grid .disc svg{width:30px;height:30px}
</style>
</head>
<body>

<svg width="0" height="0" style="position:absolute">
  <defs>
    <symbol id="bell" viewBox="0 0 40 40">
      <path d="M20 5c-6 0-10 4.5-10 11v7l-4 5h28l-4-5v-7c0-6.5-4-11-10-11z" fill="var(--amber)"/>
      <path d="M20 5c6 0 10 4.5 10 11v7l4 5H20z" fill="var(--amber-dark)"/>
      <circle cx="20" cy="31.5" r="3.5" fill="var(--amber-dark)"/>
      <circle cx="20" cy="4" r="2" fill="var(--amber-dark)"/>
    </symbol>
    <symbol id="i-news" viewBox="0 0 24 24"><rect x="3" y="4" width="15" height="16" rx="1" fill="none" stroke="currentColor" stroke-width="1.8"/><path d="M18 8h3v10a2 2 0 0 1-4 0" fill="none" stroke="currentColor" stroke-width="1.8"/><path d="M6 8h9M6 12h9M6 16h6" stroke="currentColor" stroke-width="1.8"/></symbol>
    <symbol id="i-local" viewBox="0 0 24 24"><rect x="3" y="5" width="18" height="12" rx="1" fill="none" stroke="currentColor" stroke-width="1.8"/><path d="M6 9h6M6 13h4M14 9h4v4h-4z" stroke="currentColor" stroke-width="1.6" fill="none"/><path d="M8 20h8" stroke="currentColor" stroke-width="1.8"/></symbol>
    <symbol id="i-sport" viewBox="0 0 24 24"><circle cx="12" cy="12" r="8.5" fill="none" stroke="currentColor" stroke-width="1.8"/><path d="M3.5 12h17M12 3.5v17M6 6c3 3 3 9 0 12M18 6c-3 3-3 9 0 12" fill="none" stroke="currentColor" stroke-width="1.4"/></symbol>
    <symbol id="i-pin" viewBox="0 0 24 24"><path d="M12 21s-6-6.5-6-11a6 6 0 0 1 12 0c0 4.5-6 11-6 11z" fill="none" stroke="currentColor" stroke-width="1.8"/><circle cx="12" cy="10" r="2.3" fill="currentColor"/></symbol>
    <symbol id="i-sun" viewBox="0 0 24 24"><path d="M6 15a6 6 0 0 1 12 0z" fill="none" stroke="currentColor" stroke-width="1.8"/><path d="M12 4v3M4.5 8l2 2M19.5 8l-2 2M2 15h3M19 15h3M5 19h14" stroke="currentColor" stroke-width="1.8"/></symbol>
    <symbol id="i-deal" viewBox="0 0 24 24"><path d="M2 11l5-4 4 2 4-2 7 4-6 6-3-2-3 2z" fill="none" stroke="currentColor" stroke-width="1.7" stroke-linejoin="round"/><path d="M9 12l3 2.5M11 10l3 2.5" stroke="currentColor" stroke-width="1.4"/></symbol>
    <symbol id="t-on" viewBox="0 0 22 22"><circle cx="11" cy="11" r="10.5" fill="var(--purple)"/><path d="M6.5 11.3l3 3 6-6.3" fill="none" stroke="var(--white)" stroke-width="2"/></symbol>
    <symbol id="t-off" viewBox="0 0 22 22"><circle cx="11" cy="11" r="10.5" fill="var(--off)"/><path d="M7.5 7.5l7 7M14.5 7.5l-7 7" stroke="var(--white)" stroke-width="2"/></symbol>
    <symbol id="back" viewBox="0 0 20 20"><circle cx="10" cy="10" r="8.5" fill="none" stroke="var(--white)" stroke-width="1.6"/><path d="M11.5 6L7.5 10l4 4" fill="none" stroke="var(--white)" stroke-width="1.8"/></symbol>
  </defs>
</svg>

<!-- Intro screen, header variant -->
<section class="screen screen--tl">
  <div class="backdrop backdrop--intro" role="img" aria-label="Soft purple mountain landscape fading into pale lilac"></div>
  <div class="status-bar"><span>●●●●○ Corvane</span><span class="time">4:21 PM</span><span>100%<i class="battery"></i></span></div>
  <h1 class="intro-title">NOTIFICATIONS</h1>
  <svg class="bell-badge" viewBox="0 0 130 130" aria-hidden="true">
    <circle cx="65" cy="65" r="62" fill="var(--white)"/>
    <use href="#bell" x="28" y="24" width="74" height="74"/>
    <circle cx="104" cy="100" r="14" fill="var(--alert)"/>
    <rect x="102.5" y="91" width="3" height="11" rx="1" fill="var(--white)"/>
    <circle cx="104" cy="106" r="1.8" fill="var(--white)"/>
  </svg>
  <div class="intro-copy" style="top:330px">
    <p>By enabling push notifications, you can keep up to date with occasional notifications related to items you care about. Select the categories on the next screen and then authorize the push notifications.</p>
    <p>If you ever change your mind, you can adjust these options in the <strong>Settings Menu</strong> of this app.</p>
  </div>
  <div class="next-bar">NEXT</div>
</section>

<!-- Category list screen -->
<section class="screen screen--tr">
  <div class="backdrop backdrop--header" role="img" aria-label="Purple mountain landscape header"></div>
  <div class="status-bar"><span>●●●●○ Corvane</span><span class="time">7:28 PM</span><span>100%<i class="battery"></i></span></div>
  <header class="app-header"><svg class="back"><use href="#back"/></svg>Push Notifications</header>
  <p class="prompt prompt--small">Select the categories that you wish to<br>receive occasional notices</p>
  <svg class="mini-bell" viewBox="0 0 72 72" aria-hidden="true">
    <circle cx="36" cy="36" r="34" fill="var(--white)"/>
    <use href="#bell" x="14" y="14" width="38" height="38"/>
    <path d="M50 30h10M50 36h12M50 42h10" stroke="var(--ink-soft)" stroke-width="2.5"/>
  </svg>
  <ul class="category-list" style="color:var(--ink-soft)">
    <li><svg class="icon"><use href="#i-news"/></svg><span class="label">Breaking News</span><svg class="toggle"><use href="#t-on"/></svg></li>
    <li><svg class="icon"><use href="#i-local"/></svg><span class="label">Local News</span><svg class="toggle"><use href="#t-on"/></svg></li>
    <li><svg class="icon"><use href="#i-sport"/></svg><span class="label">Sports</span><svg class="toggle"><use href="#t-off"/></svg></li>
    <li><svg class="icon"><use href="#i-pin"/></svg><span class="label">Local Events</span><svg class="toggle"><use href="#t-off"/></svg></li>
    <li><svg class="icon"><use href="#i-sun"/></svg><span class="label">Weather Alerts</span><svg class="toggle"><use href="#t-on"/></svg></li>
    <li><svg class="icon"><use href="#i-deal"/></svg><span class="label">Local Deals</span><svg class="toggle"><use href="#t-off"/></svg></li>
  </ul>
  <div class="enable-row enable-row--list"><svg><use href="#t-on"/></svg>Enable these categories on the next screen</div>
  <div class="next-bar">NEXT</div>
</section>

<!-- Intro screen, button variant -->
<section class="screen screen--bl">
  <div class="backdrop backdrop--intro-alt" role="img" aria-label="Purple mountain landscape fading into pale teal"></div>
  <div class="status-bar"><span>●●●●○ Corvane</span><span class="time">4:21 PM</span><span>100%<i class="battery"></i></span></div>
  <h1 class="intro-title">NOTIFICATIONS</h1>
  <svg class="bell-badge" viewBox="0 0 130 130" aria-hidden="true">
    <circle cx="65" cy="65" r="62" fill="var(--white)"/>
    <use href="#bell" x="28" y="24" width="74" height="74"/>
    <circle cx="104" cy="100" r="14" fill="var(--alert)"/>
    <rect x="102.5" y="91" width="3" height="11" rx="1" fill="var(--white)"/>
    <circle cx="104" cy="106" r="1.8" fill="var(--white)"/>
  </svg>
  <div class="intro-copy" style="top:352px">
    <p>By enabling push notifications, you can keep up to date with occasional notifications related to items you care about. Select the categories on the next screen and then authorize the push notifications.</p>
    <p>If you ever change your mind, you can adjust these options in the <strong>Settings Menu</strong> of this app.</p>
  </div>
  <div class="next-button">NEXT</div>
</section>

<!-- Category grid screen -->
<section class="screen screen--br">
  <div class="backdrop backdrop--full" role="img" aria-label="Deep purple mountain landscape"></div>
  <div class="status-bar"><span>●●●●○ Corvane</span><span class="time">7:28 PM</span><span>100%<i class="battery"></i></span></div>
  <header class="app-header"><svg class="back"><use href="#back"/></svg>Push Notifications</header>
  <p class="prompt prompt--large">Select the categories that you wish to<br>receive occasional notices</p>
  <ul class="category-grid">
    <li><span class="disc" style="color:var(--purple)"><svg><use href="#i-news"/></svg></span>Breaking News</li>
    <li><span class="disc" style="color:var(--purple)"><svg><use href="#i-local"/></svg></span>Local News</li>
    <li><span class="disc" style="color:var(--purple)"><svg><use href="#i-sport"/></svg></span>Sports</li>
    <li><span class="disc" style="color:var(--purple)"><svg><use href="#i-pin"/></svg></span>Local Events</li>
    <li><span class="disc" style="color:var(--purple)"><svg><use href="#i-sun"/></svg></span>Weather Alerts</li>
    <li><span class="disc" style="color:var(--purple)"><svg><use href="#i-deal"/></svg></span>Local Deals</li>
  </ul>
  <div class="enable-row enable-row--grid"><svg><use href="#t-on"/></svg>Enable these categories on the next screen</div>
  <div class="next-bar next-bar--deep">NEXT</div>
</section>

</body>
</html>
```